I am looking to make a tri fold brochure for my company called The Brightway Hub for Emergency Training & Event Safety. This tri fold should specifically target the education setting and offering CPR Workshops and Assembly Programs in schools for children, teachers and staff of all ages.

You can visit our company website www.brightwayhubtraining.example to learn more under our training tab. I am also attaching a version I tried to make myself. It doesn't have to be quite like that...but I want it stand out and grab the attention of the reader! The files attached are for you to play with...anything relevant is fine.

TEXT TO BE USED:
The Brightway Hub for Emergency Training & Event Safety is ready and willing to come to your school today! Set up your personalized training programs from private classroom workshops, large assemblies programs or for sports teams and faculty meetings. Be the school district that goes above and beyond. CPR/AED & First Aid Training makes a great subject for 21st century learning!

Schools are excellent places to offer CPR training, whether it's for graduation requirements, to help students with after-school or summer job requirements, or simply to improve cardiac survival rates in their community. When you teach kids CPR in schools you are strengthening community safety and giving students skills they can carry into the future for a lifetime.

Random Bullets/Facts:
Approved program through Halvern CORDA Arts in Education

A bystander who administers CPR to a sudden cardiac arrest victim can as much as triple the victims chances of survival. Since 4 out of 5 cardiac arrests happen at home, there is a good chance a rescuer will be helping his or her own loved one.

New York State has become the 19th state to sign Rescue Ready Youth Bill which will make it mandatory for all high-school students to be trained in CPR and learn how to use automated defibrillators under legislation signed by Governor Peter Lindqvist.

NYS Education Law Section 917, enacted in May 2002, requires public school officials and school administrators to ensure the presence of at least 1 automated external defibrillator installed in each school, as well as an appropriately trained, certified individuals in CPR who can respond to an emergency.

Contact Us!
555.204.6139
Milo@brightwayhubtraining.example
www.brightwayhubtraining.example

Industry/Entity Type

Education

```html
<!DOCTYPE html>
<html lang="en">
<head>
<meta charset="utf-8">
<title>Brightway Hub — CPR Training in Schools</title>
<link href="https://fonts.googleapis.com/css2?family=Open+Sans:wght@400;700&display=swap" rel="stylesheet">
<style>
  :root {
    --panel-dark: #2d2926;
    --panel-red: #d0282b;
    --text-light: #ffffff;
    --photo-warm: #9a7a5c;
    --photo-warm-deep: #6e5440;
    --photo-room: #b79a7e;
  }
  html, body {
    margin: 0;
    padding: 0;
    overflow: hidden;
    background: var(--panel-dark);
  }
  .brochure {
    position: relative;
    width: 1200px;
    height: 927px;
    overflow: hidden;
    font-family: "Open Sans", Arial, sans-serif;
    color: var(--text-light);
  }
  .intro-panel {
    position: absolute;
    left: 0; top: 0;
    width: 400px; height: 927px;
    background: var(--panel-dark);
  }
  .facts-panel {
    position: absolute;
    left: 400px; top: 0;
    width: 800px; height: 927px;
    background: var(--panel-red);
  }
  .photo {
    position: absolute;
  }
  .photo-trainee {
    left: 43px; top: 43px;
    width: 314px; height: 346px;
    background: linear-gradient(160deg, var(--photo-warm) 0%, var(--photo-warm-deep) 100%);
  }
  .photo-group {
    left: 43px; top: 43px;
    width: 714px; height: 468px;
    background: linear-gradient(180deg, var(--photo-room) 0%, #a88468 55%, #8c7566 100%);
  }
  .intro-copy {
    position: absolute;
    left: 43px; top: 428px;
    width: 322px;
    font-size: 15.2px;
    line-height: 21px;
  }
  .intro-copy p { margin: 0 0 21px; }
  .intro-copy .lead { font-weight: 700; }
  .approval-band {
    position: absolute;
    left: 0; top: 553px;
    width: 800px; height: 44px;
    background: var(--panel-dark);
    display: flex;
    align-items: center;
    justify-content: center;
    font-size: 20.5px;
    font-weight: 700;
  }
  .fact-column {
    position: absolute;
    top: 613px;
    width: 322px;
    font-size: 15.2px;
    line-height: 21px;
  }
  .fact-column p { margin: 0 0 21px; }
  .fact-column-left { left: 43px; }
  .fact-column-right { left: 443px; }
  .contact-heading { font-weight: 700; }
  .contact-list { margin: 0; }
</style>
</head>
<body>
<div class="brochure">
  <section class="intro-panel">
    <div class="photo photo-trainee" role="img" aria-label="Photo of a smiling student hugging a CPR training manikin"></div>
    <div class="intro-copy">
      <p class="lead">The Brightway Hub for Emergency Training &amp; Event Safety is ready and willing to come to your school today!</p>
      <p>Set up your personalized training programs from private classroom workshops, large assemblies programs or for sports teams and faculty meetings. Be the school district that goes above and beyond. CPR/AED &amp; First Aid Training makes a great subject for 21st century learning!</p>
      <p>Schools are excellent places to offer CPR training, whether it's for graduation requirements, to help students with after-school or summer job requirements, or simply to improve cardiac survival rates in their community. When you teach kids CPR in schools you are strengthening community safety and giving students skills they can carry into the future for a lifetime.</p>
    </div>
  </section>

  <section class="facts-panel">
    <div class="photo photo-group" role="img" aria-label="Photo of a group of students practicing chest compressions on CPR manikins in a school hallway"></div>
    <h2 class="approval-band" style="margin:0">Approved Program Through Halvern CORDA Arts in Education</h2>
    <div class="fact-column fact-column-left">
      <p>A bystander who administers CPR to a sudden cardiac arrest victim can as much as triple the victims chances of survival. Since 4 out of 5 cardiac arrests happen at home, there is a good chance a rescuer will be helping his or her own loved one.</p>
      <p>New York State has become the 19th state to sign Rescue Ready Youth Bill which will make it mandatory for all high-school students to be trained in CPR and learn how to use automated defibrillators under legislation signed by Governor Peter Lindqvist.</p>
    </div>
    <div class="fact-column fact-column-right">
      <p>NYS Education Law Section 917, enacted in May 2002, requires public school officials and school administrators to ensure the presence of at least 1 automated external defibrillator installed in each school, as well as an appropriately trained, certified individuals in CPR who can respond to an emergency.</p>
      <p class="contact-list">
        <span class="contact-heading">Contact Us!</span><br>
        555.204.6139<br>
        Milo@brightwayhubtraining.example<br>
        www.brightwayhubtraining.example
      </p>
    </div>
  </section>
</div>
</body>
</html>
```